1. Overview of company:
Copper Fern Mobile solutions private Ltd is one of the leading innovators & providers of Value added services (VAS) and telecom solutions to the top telecom operators across the world. We are the pioneer of several telecom technologies and products with our solutions empowering over 40 telecom giant in 51 countries.

2. Product Overview:
Vocal Twist is the most innovative voice morphing mobile app that has revolutionized the concept of IVR based offerings for telecom operators across the world. It lets you talk to your friend in a voice of your choice at just the press of a button. In addition to every call, users can now speak to their friends with background sounds of their choice.

In simple words: If person A calls person B, person A can choose the voice he wants B to listen, Words and sentences remain same just the voice changes. Person A can even activate a background sound for both of them while talking.

3. Objective of the design:
The purpose of this campaign is to establish Vocal Twist as Innovative, Lively, Youthful, Fun mobile app generally used for spreading smiles via pranks. The primary objective is to persuade the audience to download and use Vocal Twist mobile app, as well as to spread and characterize this new app.

4. Product layout:
Page 1: Landing Page
- pictorial explanation, what Vocal Twist stands for

Page 2: Home Screen options
-Navigation to vocal twist
-Navigation to sound scenery

Page 3: Vocal Twist options
-Female
-Cartoon
-King
-Bunny

Page 4: Sound scenery options
-Romantic
-Airport
-Traffic
-Football
-Church
-Beach

5. Target Audience
The users of the mobile app will be teenager whose age ranges from 16-27. The demographics are not restricted to a particular country and will be present on global level.

6. Deliverable
- 4 Uncoded screen and icon for mobile app "Vocal Twist"
- Our company name is "Copper Fern" , we would like to see designs that use Black and Green, at the same time its not mandatory.
-Design should communicate what the app stands for "Changing voice of caller"

Target Market(s)

User of the mobile app will be teenagers whose age ranges from 16-27. The demographics are not restricted to a particular country and will be present on global level. It's for masses.

Industry/Entity Type

Telecommunications

Requirements
Must have
• The design should be self explanatory, what the app stands for.
• Editable format for integration purpose.
Nice to have
• Would prefer Icons and very few words.
• Professional, elegant at the same time trendy designs.

```html
<!DOCTYPE html>
<html lang="en">
<head>
<meta charset="utf-8">
<title>Vocal Twist – Home</title>
<link rel="stylesheet" href="https://fonts.googleapis.com/css2?family=Patrick+Hand&family=Questrial&display=swap">
<style>
  :root {
    --canvas-bg: #e6e5e1;
    --screen-bg: #f1f1f1;
    --header-green: #8db350;
    --header-text: #ffffff;
    --divider: #c9c9c9;
    --label-text: #3a3a3a;
    --option-text: #9a9a9a;
    --dot-green: #a9c97a;
    --dot-ring: #d3e4bb;
    --voice-tile: #dea13b;
    --voice-tile-dark: #d08f2a;
    --ambiance-tile: #ebb4c2;
    --ambiance-tile-dark: #e2a1b2;
    --icon-dark: #2f2f2f;
    --icon-light: #ffffff;
  }
  * { box-sizing: border-box; margin: 0; padding: 0; }
  html, body {
    width: 1200px;
    height: 1000px;
    overflow: hidden;
    background: var(--canvas-bg);
  }
  .canvas { position: relative; width: 1200px; height: 1000px; }
  .app-screen {
    position: absolute;
    left: 360px; top: 74px;
    width: 480px; height: 852px;
    background: var(--screen-bg);
    overflow: hidden;
    box-shadow: 0 10px 40px rgba(0,0,0,0.12);
  }
  .app-header { position: absolute; left: 0; top: 0; width: 480px; height: 112px; }
  .app-header svg.header-band { position: absolute; left: 0; top: 0; }
  .status-bar {
    position: absolute; left: 0; top: 0;
    width: 100%; height: 28px;
    display: flex; align-items: center; justify-content: space-between;
    padding: 0 12px;
    color: var(--header-text);
    font-family: "Questrial", sans-serif;
    font-size: 14px;
  }
  .signal-dots { display: flex; gap: 3px; }
  .signal-dots span { width: 6px; height: 6px; border-radius: 50%; background: var(--header-text); }
  .status-time { font-weight: 700; letter-spacing: 0.3px; }
  .battery { display: flex; align-items: center; gap: 5px; }
  .battery-icon {
    width: 26px; height: 11px;
    border: 1px solid var(--header-text);
    border-radius: 2px; padding: 1px; position: relative;
  }
  .battery-icon::before { content: ""; display: block; width: 100%; height: 100%; background: var(--header-text); }
  .battery-icon::after {
    content: ""; position: absolute; right: -4px; top: 3px;
    width: 2px; height: 4px; background: var(--header-text);
  }
  .screen-title {
    position: absolute; left: 0; top: 36px; width: 100%;
    text-align: center;
    font-family: "Patrick Hand", cursive;
    font-weight: 400;
    font-size: 32px;
    color: var(--header-text);
  }
  .option-section { position: absolute; left: 0; width: 480px; }
  .option-section.voice { top: 112px; height: 300px; border-bottom: 1.5px solid var(--divider); }
  .option-section.ambiance { top: 412px; height: 440px; }
  .option-tile {
    position: absolute;
    left: 165px; width: 150px; height: 150px;
    border-radius: 14px;
    overflow: hidden;
  }
  .option-tile svg { display: block; width: 100%; height: 100%; }
  .voice .option-tile {
    top: 65px;
    background: linear-gradient(160deg, var(--voice-tile), var(--voice-tile-dark));
  }
  .ambiance .option-tile {
    top: 60px; left: 163px;
    width: 152px; height: 162px;
    background: linear-gradient(160deg, var(--ambiance-tile), var(--ambiance-tile-dark));
  }
  .option-label {
    position: absolute; left: 0; width: 100%;
    text-align: center;
    font-family: "Questrial", sans-serif;
    font-size: 16px;
    color: var(--label-text);
  }
  .voice .option-label { top: 220px; }
  .ambiance .option-label { top: 228px; }
  .current-choice {
    position: absolute; right: 22px;
    display: flex; align-items: center; gap: 8px;
    font-family: "Patrick Hand", cursive;
    font-size: 19px;
    color: var(--option-text);
  }
  .voice .current-choice { top: 262px; }
  .ambiance .current-choice { top: 270px; }
  .choice-dot {
    width: 14px; height: 14px; border-radius: 50%;
    background: var(--dot-green);
    box-shadow: 0 0 0 2px var(--dot-ring);
  }
</style>
</head>
<body>
<div class="canvas">
  <main class="app-screen">
    <header class="app-header">
      <svg class="header-band" width="480" height="112" viewBox="0 0 480 112">
        <path d="M0 0 H480 V102 C420 98 360 106 300 103 C220 99 150 108 80 104 C50 102 25 107 0 105 Z" fill="var(--header-green)"/>
      </svg>
      <div class="status-bar">
        <div class="signal-dots"><span></span><span></span><span></span><span></span><span></span></div>
        <div class="status-time">12:49 PM</div>
        <div class="battery">100% <div class="battery-icon"></div></div>
      </div>
      <h1 class="screen-title">Home</h1>
    </header>

    <section class="option-section voice">
      <div class="option-tile" role="img" aria-label="Voice selection: cartoon character voice with a sound wave">
        <svg viewBox="0 0 150 150" aria-hidden="true">
          <g class="mic-icon" fill="none" stroke="var(--icon-dark)" stroke-width="5" stroke-linecap="round">
            <rect x="62" y="22" width="26" height="46" rx="13" fill="var(--icon-dark)"/>
            <path d="M50 54 a25 25 0 0 0 50 0"/>
            <line x1="75" y1="79" x2="75" y2="92"/>
            <line x1="63" y1="93" x2="87" y2="93"/>
          </g>
          <g class="sound-wave" stroke="var(--icon-light)" stroke-width="3" stroke-linecap="round">
            <line x1="30" y1="124" x2="30" y2="128"/>
            <line x1="37" y1="121" x2="37" y2="131"/>
            <line x1="44" y1="118" x2="44" y2="134"/>
            <line x1="51" y1="122" x2="51" y2="130"/>
            <line x1="58" y1="114" x2="58" y2="138"/>
            <line x1="65" y1="119" x2="65" y2="133"/>
            <line x1="72" y1="112" x2="72" y2="140"/>
            <line x1="79" y1="117" x2="79" y2="135"/>
            <line x1="86" y1="114" x2="86" y2="138"/>
            <line x1="93" y1="120" x2="93" y2="132"/>
            <line x1="100" y1="117" x2="100" y2="135"/>
            <line x1="107" y1="122" x2="107" y2="130"/>
            <line x1="114" y1="120" x2="114" y2="132"/>
            <line x1="121" y1="124" x2="121" y2="128"/>
          </g>
        </svg>
      </div>
      <p class="option-label">select the voice</p>
      <div class="current-choice">Cartoon <span class="choice-dot"></span></div>
    </section>

    <section class="option-section ambiance">
      <div class="option-tile" role="img" aria-label="Ambiance selection: romantic music with notes and hearts">
        <svg viewBox="0 0 152 162" aria-hidden="true">
          <g class="music-note" fill="var(--icon-dark)" stroke="var(--icon-dark)" stroke-width="5" stroke-linecap="round">
            <line x1="64" y1="112" x2="64" y2="50" />
            <line x1="110" y1="102" x2="110" y2="40" />
            <path d="M64 50 L110 40 L110 56 L64 66 Z" stroke-linejoin="round"/>
            <ellipse cx="53" cy="113" rx="13" ry="10" stroke="none"/>
            <ellipse cx="99" cy="103" rx="13" ry="10" stroke="none"/>
          </g>
          <g class="hearts" fill="var(--icon-light)">
            <path d="M120 22 c-3-5-11-3-9 3 c1 4 9 9 9 9 s8-5 9-9 c2-6-6-8-9-3z"/>
            <path d="M134 38 c-2-3-7-2-6 2 c1 3 6 6 6 6 s5-3 6-6 c1-4-4-5-6-2z"/>
          </g>
        </svg>
      </div>
      <p class="option-label">select the ambiance</p>
      <div class="current-choice">Romantic <span class="choice-dot"></span></div>
    </section>
  </main>
</div>
</body>
</html>
```